Design range of flavoured vodka soda cans

We need help designing a range of flavoured vodka soda cans.
Our company is www.carrowbeacon.com.au
Vodka soda flavours include;
- Raspberry
- Grape
- Blueberry
- Pina Colada
- Musk
- Lime
- Pineapple
- Watermelon
- Tropical Punch
- Honeycomb
- Pineapple and Lime

Plus separately a cocktail range including;
- Berry Fizzle
- Espresso Martini
- Candywheel
- Swirlo
- Passionfruit Gin and Tonic
- Signature Gin and Tonic

Can specifications attached

3.5% ALC/VOL
250ml Cans

Target Market(s)

25-35 Mainly Female

Industry/Entity Type

Alcoholic Beverages

Requirements
Must have
• Clear logo, room for a barcode to be added, 250ml and 3.5% ALC/VOL on the front centre, Australian pregnancy warning logo see attachments, 0.79 standard drink logo, simple description, "Produced By: Carrow Beacon Pty Ltd 9/22 Tamblin Crescent Edgeworth NSW 2285"
Nice to have
• Simple consistent design for the range, fresh look, vibrant
Should not have
• Cartoon characters or anything perceived to be attractive to minors

```html
<!DOCTYPE html>
<html lang="en">
<head>
<meta charset="utf-8">
<title>Carrow Beacon Vodka Soda Range</title>
<link href="https://fonts.googleapis.com/css2?family=Fredoka:wght@700&family=Montserrat:wght@500;600;700;800&family=Barlow+Condensed:wght@700&family=Sacramento&display=swap" rel="stylesheet">
<style>
  :root {
    --page: #e9e9eb;
    --label-white: #f7f7f8;
    --ink: #141414;
    --grape: #4f2c82;
    --grape-deep: #2c1450;
    --raspberry: #c8142f;
    --raspberry-deep: #7a0614;
    --blueberry: #1c3190;
    --blueberry-deep: #0c1650;
  }
  * { box-sizing: border-box; margin: 0; padding: 0; }
  html, body { width: 1179px; height: 1200px; overflow: hidden; }
  body {
    background: var(--page);
    display: flex;
    justify-content: center;
    align-items: center;
    gap: 24px;
    font-family: "Montserrat", sans-serif;
  }
  .can-label {
    position: relative;
    width: 365px;
    height: 1120px;
    background: var(--label-white);
    overflow: hidden;
    box-shadow: 0 6px 18px rgba(0,0,0,0.12);
    color: var(--brand);
  }
  .can-label--grape { --brand: var(--grape); --brand-deep: var(--grape-deep); }
  .can-label--raspberry { --brand: var(--raspberry); --brand-deep: var(--raspberry-deep); }
  .can-label--blueberry { --brand: var(--blueberry); --brand-deep: var(--blueberry-deep); }

  .rim-band {
    height: 64px;
    background: linear-gradient(180deg, var(--brand), var(--brand-deep));
    display: flex; align-items: center; justify-content: center; gap: 18px;
    color: #fff; font-weight: 600; font-size: 14px; letter-spacing: 0.3px;
  }
  .rim-band .dot { width: 9px; height: 9px; border-radius: 50%; background: #fff; }

  .brand-name {
    margin-top: 52px;
    text-align: center;
    font-weight: 600;
    font-size: 32px;
    color: var(--ink);
    letter-spacing: 0.5px;
  }

  .product-title {
    margin-top: 46px;
    text-align: center;
    font-family: "Fredoka", sans-serif;
    font-weight: 700;
    line-height: 1.02;
    color: var(--brand);
    -webkit-text-stroke: 2px #fff;
    paint-order: fill stroke;
    text-shadow:
      2px 0 0 var(--brand-deep), -2px 0 0 var(--brand-deep),
      0 2px 0 var(--brand-deep), 0 -2px 0 var(--brand-deep),
      4px 4px 0 var(--brand-deep), 5px 5px 0 var(--brand-deep);
  }
  .product-title .line-vodka { display: block; font-size: 100px; letter-spacing: 1px; }
  .product-title .line-soda { display: block; font-size: 100px; letter-spacing: 2px; }

  .flavour-ribbon {
    margin: 34px auto 0;
    display: flex; align-items: center; justify-content: center; gap: 10px;
  }
  .flavour-ribbon .rule { display: flex; flex-direction: column; gap: 7px; }
  .flavour-ribbon .rule span { display: block; width: 38px; height: 3px; background: var(--ink); }
  .flavour-ribbon .tag {
    background: var(--ink); color: #fff;
    font-family: "Barlow Condensed", sans-serif; font-weight: 700;
    font-size: 34px; letter-spacing: 1px;
    padding: 4px 34px 2px;
    clip-path: polygon(0 0, 100% 0, 94% 50%, 100% 100%, 0 100%, 6% 50%);
  }

  .strength-row {
    position: relative;
    margin-top: 44px;
    height: 120px;
    display: flex; align-items: center; justify-content: center;
  }
  .strength-row .stripes {
    position: absolute; left: 0; right: 0; top: 36px; height: 48px;
    background: repeating-linear-gradient(180deg, var(--brand) 0 10px, transparent 10px 19px);
  }
  .strength-badge { position: relative; width: 124px; height: 124px; color: var(--brand); }

  .story-panel {
    position: absolute; left: 0; right: 0; bottom: 0; height: 370px;
    background: linear-gradient(180deg, var(--brand), var(--brand-deep));
    color: #fff; text-align: center;
    padding-top: 30px;
  }
  .story-panel .story-heading {
    font-family: "Sacramento", cursive;
    font-size: 54px; line-height: 1;
  }
  .story-panel .story-copy {
    margin: 16px 22px 0;
    font-size: 14px; font-weight: 500; line-height: 1.65;
  }
  .compliance-row {
    margin-top: 20px;
    display: flex; justify-content: center; align-items: center; gap: 18px;
  }
  .pregnancy-mark {
    width: 40px; height: 40px; border-radius: 50%;
    background: #fff;
  }
  .standard-drinks {
    display: flex; align-items: center; gap: 8px;
    font-size: 11px; font-weight: 700; line-height: 1.15; text-align: left;
  }
  .standard-drinks .drinks-mark {
    width: 40px; height: 40px; background: #fff; color: var(--ink);
    display: flex; align-items: center; justify-content: center;
    font-size: 13px; font-weight: 800;
  }
  .producer {
    margin: 14px 20px 0;
    font-size: 10.5px; font-weight: 500; line-height: 1.45;
  }
  .story-panel .net-volume {
    position: absolute; left: 0; right: 0; bottom: 20px;
    display: flex; justify-content: center; gap: 22px;
    font-weight: 800; font-size: 20px; letter-spacing: 0.5px;
  }
</style>
</head>
<body>

<svg width="0" height="0" style="position:absolute" aria-hidden="true">
  <defs>
    <path id="arc-top" d="M24,62 A38,38 0 0 1 100,62"/>
    <path id="arc-bottom" d="M18,62 A44,44 0 0 0 106,62"/>
    <symbol id="abv-badge" viewBox="0 0 124 124">
      <circle cx="62" cy="62" r="60" fill="currentColor"/>
      <circle cx="62" cy="62" r="33" fill="#fff"/>
      <circle cx="13" cy="62" r="2.5" fill="#fff"/>
      <circle cx="111" cy="62" r="2.5" fill="#fff"/>
      <text font-family="Montserrat, sans-serif" font-weight="700" font-size="13" fill="#fff" letter-spacing="3">
        <textPath href="#arc-top" startOffset="50%" text-anchor="middle">ALCOHOL</textPath>
      </text>
      <text font-family="Montserrat, sans-serif" font-weight="700" font-size="13" fill="#fff" letter-spacing="3" dy="10">
        <textPath href="#arc-bottom" startOffset="50%" text-anchor="middle">BY VOLUME</textPath>
      </text>
      <text x="62" y="70" text-anchor="middle" font-family="Montserrat, sans-serif" font-weight="800" font-size="21" fill="#141414">3.5%</text>
    </symbol>
  </defs>
</svg>

<section class="can-label can-label--grape">
  <div class="rim-band"><span class="dot"></span>LOREM IPSUM DOLOR SIT<span class="dot"></span></div>
  <div class="brand-name">Carrow Beacon</div>
  <h1 class="product-title"><span class="line-vodka">VODKA</span><span class="line-soda">SODA</span></h1>
  <div class="flavour-ribbon">
    <div class="rule"><span></span><span></span></div>
    <div class="tag">GRAPE</div>
    <div class="rule"><span></span><span></span></div>
  </div>
  <div class="strength-row">
    <div class="stripes"></div>
    <svg class="strength-badge" viewBox="0 0 124 124" role="img" aria-label="3.5% alcohol by volume"><use href="#abv-badge"/></svg>
  </div>
  <div class="story-panel">
    <p class="story-heading">Lorem ipsum dolor</p>
    <p class="story-copy">Lorem ipsum dolor sit amet, consectetur adipiscing elit, sed do eiusmod tempor incididunt ut labore et dolore magna aliqua.</p>
    <div class="compliance-row">
      <div class="pregnancy-mark" role="img" aria-label="Pregnancy warning mark"></div>
      <div class="standard-drinks"><div class="drinks-mark">0.79</div>STANDARD<br>DRINKS</div>
    </div>
    <p class="producer">Produced By: Carrow Beacon Pty Ltd<br>9/22 Tamblin Crescent Edgeworth NSW 2285</p>
    <p class="net-volume"><span>250ML</span><span>3.5% ALC/VOL</span></p>
  </div>
</section>

<section class="can-label can-label--raspberry">
  <div class="rim-band"><span class="dot"></span>LOREM IPSUM DOLOR SIT<span class="dot"></span></div>
  <div class="brand-name">Carrow Beacon</div>
  <h1 class="product-title"><span class="line-vodka">VODKA</span><span class="line-soda">SODA</span></h1>
  <div class="flavour-ribbon">
    <div class="rule"><span></span><span></span></div>
    <div class="tag">RASPBERRY</div>
    <div class="rule"><span></span><span></span></div>
  </div>
  <div class="strength-row">
    <div class="stripes"></div>
    <svg class="strength-badge" viewBox="0 0 124 124" role="img" aria-label="3.5% alcohol by volume"><use href="#abv-badge"/></svg>
  </div>
  <div class="story-panel">
    <p class="story-heading">Lorem ipsum dolor</p>
    <p class="story-copy">Lorem ipsum dolor sit amet, consectetur adipiscing elit, sed do eiusmod tempor incididunt ut labore et dolore magna aliqua.</p>
    <div class="compliance-row">
      <div class="pregnancy-mark" role="img" aria-label="Pregnancy warning mark"></div>
      <div class="standard-drinks"><div class="drinks-mark">0.79</div>STANDARD<br>DRINKS</div>
    </div>
    <p class="producer">Produced By: Carrow Beacon Pty Ltd<br>9/22 Tamblin Crescent Edgeworth NSW 2285</p>
    <p class="net-volume"><span>250ML</span><span>3.5% ALC/VOL</span></p>
  </div>
</section>

<section class="can-label can-label--blueberry">
  <div class="rim-band"><span class="dot"></span>LOREM IPSUM DOLOR SIT<span class="dot"></span></div>
  <div class="brand-name">Carrow Beacon</div>
  <h1 class="product-title"><span class="line-vodka">VODKA</span><span class="line-soda">SODA</span></h1>
  <div class="flavour-ribbon">
    <div class="rule"><span></span><span></span></div>
    <div class="tag">BLUEBERRY</div>
    <div class="rule"><span></span><span></span></div>
  </div>
  <div class="strength-row">
    <div class="stripes"></div>
    <svg class="strength-badge" viewBox="0 0 124 124" role="img" aria-label="3.5% alcohol by volume"><use href="#abv-badge"/></svg>
  </div>
  <div class="story-panel">
    <p class="story-heading">Lorem ipsum dolor</p>
    <p class="story-copy">Lorem ipsum dolor sit amet, consectetur adipiscing elit, sed do eiusmod tempor incididunt ut labore et dolore magna aliqua.</p>
    <div class="compliance-row">
      <div class="pregnancy-mark" role="img" aria-label="Pregnancy warning mark"></div>
      <div class="standard-drinks"><div class="drinks-mark">0.79</div>STANDARD<br>DRINKS</div>
    </div>
    <p class="producer">Produced By: Carrow Beacon Pty Ltd<br>9/22 Tamblin Crescent Edgeworth NSW 2285</p>
    <p class="net-volume"><span>250ML</span><span>3.5% ALC/VOL</span></p>
  </div>
</section>

</body>
</html>
```